label design for soy candle

I am a start up making soy candles and other products involving scents.
On the label should be in writing : Amber Dusk, Handgemacht in der Schweiz, Sojakerze, my logo with the name Pertwick Candles on it. I will upload the currant label of my candles, but I want something more fashioned. The color of the label should be black with Amber Dusk written in gold, and the rest in white. Or maybe suggest something different, I am open to new designs. I am also open to change the logo, except the flower has to stay.
Sizes : square 60x60mm / round 50mm / rectangle 70x20mm ( for different jars )

```html
<!DOCTYPE html>
<html lang="de">
<head>
<meta charset="utf-8">
<title>Pertwick Candles – Etiketten Sojakerze</title>
<link rel="stylesheet" href="https://fonts.googleapis.com/css2?family=Playfair+Display:wght@400;500&family=Open+Sans:wght@400&display=swap">
<style>
  :root {
    --page: #ffffff;
    --label-black: #07090a;
    --gold-light: #f4d9a0;
    --gold-mid: #c9ad7c;
    --gold-dark: #8e774c;
    --white: #ffffff;
    --ink: #111111;
    --gold-gradient: linear-gradient(90deg, var(--gold-light) 0%, var(--gold-mid) 45%, var(--gold-dark) 100%);
  }
  html, body {
    margin: 0;
    padding: 0;
    width: 1200px;
    height: 474px;
    overflow: hidden;
    background: var(--page);
  }
  .sheet {
    position: relative;
    width: 1200px;
    height: 474px;
    font-family: "Playfair Display", serif;
  }
  .size-note {
    position: absolute;
    transform: translateX(-50%);
    margin: 0;
    font-family: "Open Sans", sans-serif;
    font-size: 22px;
    line-height: 1;
    color: var(--ink);
    white-space: nowrap;
  }
  .label {
    position: absolute;
    box-sizing: border-box;
    background: var(--label-black);
  }
  .label-frame {
    position: absolute;
    box-sizing: border-box;
    background: var(--gold-gradient);
  }
  .label--square { left: 26px; top: 76px; width: 352px; height: 352px; }
  .frame--square { left: 22px; top: 72px; width: 360px; height: 360px; }
  .label--round { left: 416px; top: 100px; width: 290px; height: 290px; border-radius: 50%; }
  .frame--round { left: 412px; top: 96px; width: 298px; height: 298px; border-radius: 50%; }
  .label--strip { left: 765px; top: 195px; width: 414px; height: 115px; }
  .frame--strip { left: 762px; top: 192px; width: 420px; height: 121px; }

  .line {
    position: absolute;
    margin: 0;
    transform: translateX(-50%);
    white-space: nowrap;
    line-height: 1;
  }
  .brand-name {
    color: var(--white);
    font-weight: 500;
    letter-spacing: 0.03em;
  }
  .scent-name {
    font-weight: 500;
    background: var(--gold-gradient);
    -webkit-background-clip: text;
    background-clip: text;
    color: transparent;
  }
  .product-tag {
    display: flex;
    align-items: center;
    justify-content: center;
    box-sizing: border-box;
    background: var(--gold-gradient);
    color: var(--label-black);
    font-weight: 500;
    letter-spacing: 0.02em;
  }
  .origin {
    color: var(--white);
    letter-spacing: 0.09em;
  }
</style>
</head>
<body>
<main class="sheet">

  <!-- Square 60×60 mm -->
  <p class="size-note" style="left:176px; top:36px;">60x60mm</p>
  <div class="label-frame frame--square"></div>
  <section class="label label--square" aria-label="Etikett quadratisch 60x60 mm">
    <p class="line brand-name" style="left:176px; top:70px; font-size:14px;">PERTWICK CANDLES</p>
    <h2 class="line scent-name" style="left:176px; top:132px; font-size:52px;">Amber Dusk</h2>
    <p class="line product-tag" style="left:176px; top:198px; width:109px; height:27px; font-size:15px;">SOJAKERZE</p>
    <p class="line origin" style="left:176px; top:310px; font-size:12.5px;">Handgemacht in der Schweiz</p>
  </section>

  <!-- Round 50 mm -->
  <p class="size-note" style="left:561px; top:60px;">50mm</p>
  <div class="label-frame frame--round"></div>
  <section class="label label--round" aria-label="Etikett rund 50 mm">
    <p class="line brand-name" style="left:145px; top:107px; font-size:14px;">PERTWICK CANDLES</p>
    <h2 class="line scent-name" style="left:145px; top:155px; font-size:42px;">Amber Dusk</h2>
    <p class="line product-tag" style="left:145px; top:208px; width:86px; height:21px; font-size:12px;">SOJAKERZE</p>
  </section>

  <!-- Rectangle 70×20 mm -->
  <p class="size-note" style="left:905px; top:155px;">70x20mm</p>
  <div class="label-frame frame--strip"></div>
  <section class="label label--strip" aria-label="Etikett rechteckig 70x20 mm">
    <p class="line brand-name" style="left:104px; top:54px; font-size:10px;">PERTWICK CANDLES</p>
    <p class="line origin" style="left:104px; top:91px; font-size:10px;">Handgemacht in der Schweiz</p>
    <h2 class="line scent-name" style="left:306px; top:26px; font-size:37px;">Amber Dusk</h2>
    <p class="line product-tag" style="left:306px; top:71px; width:77px; height:18px; font-size:10px;">SOJAKERZE</p>
  </section>

</main>
</body>
</html>
```